Awesome business card design needed

We need a new business card design to go with our new logo.
We are a web development agency that specialises in highly complex back-end integrations as opposed to design, our customers are retailers, hotels, hospitals and any other organisation that has a large online marketing department.
Take a look at our website - www.orvekplus.com for some inspiration.
We want our new business cards to exude class, professionalism and style.
We are likely to choose a high-end card to print them on but we want the design of the card itself to really turn heads.
We have no specific colour requirements, the logo as you will see is a turquoise colour R89 G171 B167 #59aba7 but it can also be in white if you want to make the colour of the card something different.
The information on the card should be:
Name
Position
Tel
email
Potentially a double sided card could have our web address, twitter and FB links.

```html
<!DOCTYPE html>
<html lang="en">
<head>
<meta charset="utf-8">
<title>Orvekplus business card – front and back</title>
<link rel="stylesheet" href="https://fonts.googleapis.com/css2?family=Michroma&display=swap">
<style>
  :root {
    --page: #ffffff;
    --teal: #5aaea8;
    --teal-dark: #0e6b60;
    --orange: #ef7f1a;
    --white: #ffffff;
    --ink: #1f2a2a;
    --photo-dark: #2e2f31;
    --photo-light: #8c8f93;
  }
  html, body {
    margin: 0;
    padding: 0;
    width: 1200px;
    height: 408px;
    overflow: hidden;
    background: var(--page);
  }
  .canvas {
    position: relative;
    width: 1200px;
    height: 408px;
  }
  .card {
    position: absolute;
    top: 42px;
    width: 548px;
    height: 305px;
    box-shadow: 0 6px 10px rgba(0, 0, 0, 0.22);
    overflow: hidden;
  }
  .card--front { left: 42px; }
  .card--back { left: 620px; }
  .card svg { display: block; }
  .type {
    font-family: "Michroma", "Arial", sans-serif;
  }
  .fill-teal { fill: var(--teal); }
  .fill-teal-dark { fill: var(--teal-dark); }
  .fill-orange { fill: var(--orange); }
  .fill-white { fill: var(--white); }
  .fill-ink { fill: var(--ink); }
  .stop-dark { stop-color: var(--photo-dark); }
  .stop-light { stop-color: var(--photo-light); }
</style>
</head>
<body>
<main class="canvas">

  <!-- Front: web address, wordmark, social squares -->
  <section class="card card--front">
    <svg width="548" height="305" viewBox="0 0 548 305">
      <defs>
        <linearGradient id="photo-front" x1="0" y1="0" x2="1" y2="1">
          <stop offset="0" class="stop-light"/>
          <stop offset="0.55" class="stop-dark"/>
          <stop offset="1" class="stop-dark"/>
        </linearGradient>
        <clipPath id="panel-front">
          <polygon points="268,0 548,0 548,305 200,305"/>
        </clipPath>
      </defs>
      <rect class="photo" x="0" y="0" width="548" height="305" fill="url(#photo-front)" role="img" aria-label="Photo of a hand in a suit touching floating digital screens"/>

      <g clip-path="url(#panel-front)">
        <polygon class="panel fill-teal" points="268,0 548,0 548,305 200,305"/>
        <polygon class="band-top fill-teal-dark" points="268,0 548,0 548,40"/>
        <polygon class="band-orange fill-orange" points="200,223 548,274 548,305 200,305"/>

        <g class="front-content" transform="translate(270 56) rotate(8)">
          <rect class="band-white fill-white" x="-120" y="14" width="520" height="62"/>
          <text class="type web fill-ink" x="0" y="0" font-size="16" textLength="262" lengthAdjust="spacingAndGlyphs">WWW.ORVEKPLUS.COM</text>
          <text class="type wordmark fill-teal" x="-8" y="58" font-size="38" textLength="282" lengthAdjust="spacingAndGlyphs">orvekplus</text>
          <g class="social fill-white">
            <rect x="-4" y="90" width="52" height="52"/>
            <rect x="64" y="90" width="52" height="52"/>
            <rect x="132" y="90" width="52" height="52"/>
            <rect x="200" y="90" width="52" height="52"/>
          </g>
        </g>
      </g>
    </svg>
  </section>

  <!-- Back: name, position, contact details, wordmark -->
  <section class="card card--back">
    <svg width="548" height="305" viewBox="0 0 548 305">
      <defs>
        <linearGradient id="photo-back" x1="1" y1="0" x2="0" y2="1">
          <stop offset="0" class="stop-light"/>
          <stop offset="0.55" class="stop-dark"/>
          <stop offset="1" class="stop-dark"/>
        </linearGradient>
        <clipPath id="panel-back">
          <polygon points="0,0 272,0 345,305 0,305"/>
        </clipPath>
      </defs>
      <rect class="photo" x="0" y="0" width="548" height="305" fill="url(#photo-back)" role="img" aria-label="Photo of a hand in a suit touching floating digital screens"/>

      <g clip-path="url(#panel-back)">
        <polygon class="panel fill-teal" points="0,0 272,0 345,305 0,305"/>
        <polygon class="band-top fill-teal-dark" points="0,0 272,0 272,4 0,58"/>
        <polygon class="band-orange fill-orange" points="0,290 345,238 345,305 0,305"/>

        <g class="back-content" transform="translate(37 92) rotate(-10)">
          <rect class="band-white fill-white" x="-90" y="34" width="500" height="72"/>

          <text class="type name fill-ink" x="0" y="0" font-size="17" textLength="160" lengthAdjust="spacingAndGlyphs">YOUR NAME</text>
          <text class="type position fill-ink" x="14" y="20" font-size="11" textLength="88" lengthAdjust="spacingAndGlyphs">POSITION</text>

          <g class="contact fill-ink">
            <path class="icon-phone" d="M4 48 q-2 4 2 8 q4 4 8 2 l-2 -3 q-2 1 -4 -1 q-2 -2 -1 -4 z"/>
            <text class="type" x="22" y="57" font-size="12" textLength="140" lengthAdjust="spacingAndGlyphs">01 2345 6789</text>

            <rect class="icon-mobile" x="5" y="65" width="7" height="12" rx="1.5"/>
            <rect x="6.5" y="67" width="4" height="7" class="fill-white"/>
            <text class="type" x="22" y="76" font-size="12" textLength="150" lengthAdjust="spacingAndGlyphs">00 0102 0102</text>

            <rect class="icon-mail" x="3" y="86" width="12" height="8"/>
            <polyline points="3,86 9,91 15,86" fill="none" stroke="#ffffff" stroke-width="1"/>
            <text class="type" x="22" y="94" font-size="10" textLength="185" lengthAdjust="spacingAndGlyphs">EMAIL@ORVEKPLUS.COM</text>
          </g>

          <text class="type wordmark fill-white" x="8" y="146" font-size="34" textLength="256" lengthAdjust="spacingAndGlyphs">orvekplus</text>
        </g>
      </g>
    </svg>
  </section>

</main>
</body>
</html>
```